Business Card- Can you make it cool vs boring!

Need a refresh on my business card! Want it to be modern but simple, classic and a pop of coolness! we do senior living and it is boring. but that doesn't mean our business card have to look boring! Open to two sided cards. our website is www.Bruvel-HQ.com

Target Market(s)

capital market

Industry/Entity Type

senior housing/ real estate

Contact Information for Business Card

logo/ name/ cell/ address/ www.Bruvel-HQ.com/ space for a QR code

Requirements
Must have
• maybe a QR code (do not make prominent I may not use the QR so design where it can be taken out) that link to more about us/ landing page. needs to be modern but clean
Should not have
• clip art or script

```html
<!DOCTYPE html>
<html lang="en">
<head>
<meta charset="utf-8">
<title>Bruvel Living – Business Card</title>
<link href="https://fonts.googleapis.com/css2?family=Open+Sans:wght@400;600;700&display=swap" rel="stylesheet">
<style>
  :root {
    --backdrop: #afaeac;
    --card: #ffffff;
    --rust: #b14d26;
    --ink: #1b1b1b;
    --shadow: rgba(0,0,0,0.55);
  }
  html, body {
    margin: 0;
    padding: 0;
    width: 1200px;
    height: 1200px;
    overflow: hidden;
    background: var(--backdrop);
    font-family: "Open Sans", Arial, sans-serif;
  }
  .canvas {
    position: relative;
    width: 1200px;
    height: 1200px;
  }
  .card {
    position: absolute;
    left: 256px;
    width: 728px;
    height: 416px;
    background: var(--card);
    border-radius: 28px;
    overflow: hidden;
    box-shadow: 2px 5px 4px var(--shadow);
  }
  .card--front { top: 106px; }
  .card--back { top: 619px; }
  .card__band {
    position: absolute;
    left: 0;
    right: 0;
    bottom: 0;
    height: 27px;
    background: var(--rust);
  }
  .wordmark {
    position: absolute;
    color: var(--rust);
    font-weight: 600;
    white-space: nowrap;
    letter-spacing: 0.5px;
    line-height: 1;
  }
  .card--front .wordmark {
    left: 0;
    right: 0;
    top: 140px;
    text-align: center;
    font-size: 82px;
  }
  .card--back .wordmark {
    right: 40px;
    top: 72px;
    font-size: 38px;
  }
  .holder__bar {
    position: absolute;
    left: 0;
    top: 98px;
    width: 17px;
    height: 48px;
    background: var(--rust);
  }
  .holder__name {
    position: absolute;
    left: 27px;
    top: 97px;
    margin: 0;
    font-size: 26px;
    font-weight: 700;
    color: var(--rust);
    letter-spacing: -0.3px;
    line-height: 1;
  }
  .holder__role {
    position: absolute;
    left: 27px;
    top: 127px;
    margin: 0;
    font-size: 17px;
    color: var(--ink);
    line-height: 1;
  }
  .contacts {
    position: absolute;
    left: 362px;
    top: 252px;
    margin: 0;
    padding: 0;
    list-style: none;
  }
  .contacts li {
    display: flex;
    align-items: center;
    height: 26.5px;
    font-size: 18px;
    color: var(--ink);
  }
  .contacts svg {
    width: 16px;
    height: 16px;
    margin-right: 10px;
    fill: var(--rust);
    flex: none;
  }
</style>
</head>
<body>
<div class="canvas">

  <section class="card card--front">
    <div class="wordmark">Bruvel Living</div>
    <div class="card__band"></div>
  </section>

  <section class="card card--back">
    <div class="holder__bar"></div>
    <h1 class="holder__name">DARIO MENK</h1>
    <p class="holder__role">Owner</p>

    <div class="wordmark">Bruvel Living</div>

    <ul class="contacts">
      <li>
        <svg viewBox="0 0 16 16" aria-hidden="true">
          <path d="M1 6c0-2 3-3.5 7-3.5S15 4 15 6v1.2h-3.2V5.8C10.8 5.4 9.4 5.2 8 5.2s-2.8.2-3.8.6v1.4H1z"/>
          <path d="M4.5 7.5h7l2 6.5h-11z"/>
        </svg>
        (555) 014-2287
      </li>
      <li>
        <svg viewBox="0 0 16 16" aria-hidden="true">
          <path d="M0.5 3.5h15v9h-15z M2 4.5l6 4.5 6-4.5v1.2L8 10.2 2 5.7z" fill-rule="evenodd"/>
        </svg>
        info@bruvel-hq.com
      </li>
      <li>
        <svg viewBox="0 0 16 16" aria-hidden="true">
          <circle cx="8" cy="8" r="7.5"/>
          <path d="M5 3.5c1.5 0 2 1.2 1.2 2S4 6.5 4.5 8s2 1 2.2 2.5S5.5 13 5 13.5M10 3c-.5 1 .3 1.8 1.5 1.8S13 6 12 7s-2 .5-2 2 1.5 1.8 1.5 3" fill="none" stroke="#fff" stroke-width="1"/>
        </svg>
        www.bruvel-hq.com
      </li>
    </ul>

    <div class="card__band"></div>
  </section>

</div>
</body>
</html>
```